Transport & Storage Company needs a revamp of current card

Would like to keep same colours & basic design but would like to "sharpen" up look of card.

Please remove "The Brisk Haulers"

Please add 1800 417 392 on front & back of card

Please add email address on back of card - martin@ferncrestfreight.com.au

I would like our ABN No - 83 214 976 308 on back of card (which currently has logo only). Logo on back of card can be removed if insufficient space.

Please design another card (same as above) but with Renee Castlebury - 0438 752 046, renee@ferncrestfreight.com.au

I do not want cards to look "too busy" so please re-arrange layout of card if necessary.

Target Market(s)

Transport & Storage

Industry/Entity Type

It Company

Contact Information for Business Card

Please refer to attached current business card

Font styles to use
Other font styles liked:
• Tahoma

Requirements
Must have
• Refer to project decsription
Nice to have
Should not have

```html
<!DOCTYPE html>
<html lang="en">
<head>
<meta charset="utf-8">
<title>Ferncrest Freight – Business Cards</title>
<link rel="stylesheet" href="https://fonts.googleapis.com/css2?family=Open+Sans:wght@400&family=Source+Sans+3:wght@400;600;700&display=swap">
<style>
  :root {
    --sheet: #aead86;
    --card: #ffffff;
    --purple: #763a86;
    --charcoal: #58585a;
    --ink: #1d1d1f;
    --body-ink: #3a3a3c;
  }
  * { box-sizing: border-box; margin: 0; padding: 0; }
  html, body {
    width: 1200px; height: 840px; overflow: hidden;
    background: var(--sheet);
  }
  .sheet { position: relative; width: 1200px; height: 840px; }

  .card-slot { position: absolute; width: 548px; height: 320px; }
  .card-slot--front-a { left: 35px;  top: 31px; }
  .card-slot--back-a  { left: 619px; top: 31px; }
  .card-slot--front-b { left: 36px;  top: 438px; }
  .card-slot--back-b  { left: 628px; top: 440px; }

  .card {
    position: absolute; left: 0; top: 0;
    width: 685px; height: 400px;
    background: var(--card);
    transform: scale(0.8);
    transform-origin: top left;
    box-shadow: 3px 4px 6px rgba(0,0,0,0.35);
    overflow: hidden;
  }
  .card__stripes { position: absolute; inset: 0; width: 100%; height: 100%; }
  .stripe--charcoal { fill: var(--charcoal); }
  .stripe--purple { fill: var(--purple); }

  .brand {
    position: absolute;
    display: flex; align-items: center; gap: 12px;
    font-family: "Source Sans 3", sans-serif;
    font-weight: 700;
    color: var(--purple);
    white-space: nowrap;
  }
  .brand__mark { width: 30px; height: 30px; background: var(--purple); flex: none; }
  .card--front .brand { left: 36px; top: 72px; font-size: 38px; }
  .card--back .brand {
    left: 0; right: 0; top: 150px; justify-content: center; font-size: 44px;
  }
  .card--back .brand__mark { width: 36px; height: 36px; }

  .holder-name {
    position: absolute; left: 235px; top: 178px;
    font-family: "Source Sans 3", sans-serif;
    font-weight: 600; font-size: 30px;
    color: var(--purple);
  }
  .contact-list {
    position: absolute; right: 32px; top: 238px;
    list-style: none; text-align: right;
    font-family: "Open Sans", sans-serif;
    font-size: 21px; letter-spacing: 0.6px;
    color: var(--ink); line-height: 29px;
  }
  .contact-list__email { margin-top: 5px; letter-spacing: 0.4px; }

  .company-details {
    position: absolute; left: 0; right: 0; top: 230px;
    text-align: center;
    font-family: "Source Sans 3", sans-serif;
    color: var(--purple);
  }
  .company-details__abn { font-size: 15px; color: var(--body-ink); line-height: 20px; }
  .company-details__phone { font-size: 25px; margin-top: 14px; line-height: 30px; }
  .company-details__web { font-size: 25px; margin-top: 5px; line-height: 30px; }
</style>
</head>
<body>
<main class="sheet">

  <section class="card-slot card-slot--front-a">
    <article class="card card--front">
      <svg class="card__stripes" viewBox="0 0 685 400" preserveAspectRatio="none" aria-hidden="true">
        <polygon class="stripe--charcoal" points="225,0 685,0 685,63"/>
        <polygon class="stripe--charcoal" points="0,297 685,397 685,400 610,400 0,346"/>
        <polygon class="stripe--purple" points="0,356 560,400 0,400"/>
      </svg>
      <div class="brand"><span class="brand__mark"></span>Ferncrest Freight</div>
      <h2 class="holder-name">Martin Ashgrove</h2>
      <ul class="contact-list">
        <li>0452 318 607</li>
        <li>1800 417 392</li>
        <li class="contact-list__email">martin@ferncrestfreight.com.au</li>
      </ul>
    </article>
  </section>

  <section class="card-slot card-slot--back-a">
    <article class="card card--back">
      <svg class="card__stripes" viewBox="0 0 685 400" preserveAspectRatio="none" aria-hidden="true">
        <polygon class="stripe--charcoal" points="0,0 120,0 685,58 685,103"/>
        <polygon class="stripe--purple" points="170,0 685,0 685,45"/>
      </svg>
      <div class="brand"><span class="brand__mark"></span>Ferncrest Freight</div>
      <div class="company-details">
        <p class="company-details__abn">ABN No 83 214 976 308</p>
        <p class="company-details__phone">1800 417 392</p>
        <p class="company-details__web">www.ferncrestfreight.com.au</p>
      </div>
    </article>
  </section>

  <section class="card-slot card-slot--front-b">
    <article class="card card--front">
      <svg class="card__stripes" viewBox="0 0 685 400" preserveAspectRatio="none" aria-hidden="true">
        <polygon class="stripe--charcoal" points="225,0 685,0 685,63"/>
        <polygon class="stripe--charcoal" points="0,297 685,397 685,400 610,400 0,346"/>
        <polygon class="stripe--purple" points="0,356 560,400 0,400"/>
      </svg>
      <div class="brand"><span class="brand__mark"></span>Ferncrest Freight</div>
      <h2 class="holder-name">Renee Castlebury</h2>
      <ul class="contact-list">
        <li>0438 752 046</li>
        <li>1800 417 392</li>
        <li class="contact-list__email">renee@ferncrestfreight.com.au</li>
      </ul>
    </article>
  </section>

  <section class="card-slot card-slot--back-b">
    <article class="card card--back">
      <svg class="card__stripes" viewBox="0 0 685 400" preserveAspectRatio="none" aria-hidden="true">
        <polygon class="stripe--charcoal" points="0,0 120,0 685,58 685,103"/>
        <polygon class="stripe--purple" points="170,0 685,0 685,45"/>
      </svg>
      <div class="brand"><span class="brand__mark"></span>Ferncrest Freight</div>
      <div class="company-details">
        <p class="company-details__abn">ABN No 83 214 976 308</p>
        <p class="company-details__phone">1800 417 392</p>
        <p class="company-details__web">www.ferncrestfreight.com.au</p>
      </div>
    </article>
  </section>

</main>
</body>
</html>
```